The Varnel Cipher: Book Cover

I need a book cover for the English language version of a counterfactual history thriller, a story that takes off where "Greymarch" by Dalton Pike ends.

1983: Germany has won the war, the postwar time has brought prosperity and peace to Europe. The Wild East is no longer wild, only beyond the Urals do scattered Soviet units still occasionally carry out attacks against the Grenzwall administration and German settlers.
Lukas Brenning, born in Stuttgart and a criminalist with heart and soul, is district chief in Hartmannstadt a.d. Medritz, and thus simultaneously the highest police officer, judge, representative of the Reich and the KV. Ten years earlier, he had been transferred to the eastern border of the Reich in order to avoid the unpleasant consequences of his investigations into the machinations of some high-ranking Ordist party members in southern Germany. Brenning likes working in the east, but even here he can't keep his investigator's instincts in check. When a mysterious stranger turns up, Brenning's investigation brings strange things to light. The Veltrax provide the necessary information, but at the same time prevent further investigations by the KV. Despite a warning from his superiors, Brenning cannot let the file rest. When he comes across a well-kept secret about the 1940 peace treaty between Germany, England and France, events take a turn for the worse.
Brenning finds himself on the wrong side of a manhunt which he can only survive with the help of an unlikely ally.

The novel has appeared in German a couple of years ago. I need a book cover for an English language softcover book and an eBook addressed at English speakers. Please, even though the Grenzwall and Ordist party are mentioned: no swastikas and no openly National Socialist symbols.

Target Market(s)

all English speakers accross the world

Requirements
Should not have
• Swastikas and other offensive signs of the Nazi reign

```html
<!DOCTYPE html>
<html lang="en">
<head>
<meta charset="utf-8">
<title>The Varnel Cipher — Book Cover</title>
<link rel="stylesheet" href="https://fonts.googleapis.com/css2?family=Squada+One&family=Russo+One&display=swap">
<style>
  :root {
    --cover-red: #d20000;
    --figure-dark: #242424;
    --paper-white: #ffffff;
  }
  html, body {
    margin: 0;
    padding: 0;
    overflow: hidden;
    background: var(--cover-red);
  }
  .cover {
    position: relative;
    width: 800px;
    height: 1200px;
    background: var(--cover-red);
    overflow: hidden;
  }
  .cover-art,
  .title {
    position: absolute;
    inset: 0;
    width: 800px;
    height: 1200px;
  }
  .title { margin: 0; }
  .title-line {
    font-family: "Squada One", "Impact", sans-serif;
    font-weight: 400;
    font-size: 158px;
    fill: var(--paper-white);
    letter-spacing: 3px;
  }
  .author {
    position: absolute;
    top: 1088px;
    left: 0;
    width: 800px;
    margin: 0;
    text-align: center;
    font-family: "Russo One", "Arial Black", sans-serif;
    font-weight: 400;
    font-size: 54px;
    line-height: 64px;
    color: var(--paper-white);
  }
</style>
</head>
<body>
  <main class="cover">
    <svg class="cover-art" viewBox="0 0 800 1200" role="img"
         aria-label="Silhouette of a uniformed officer in a long greatcoat and peaked cap, seen from behind, with loose sheets of paper scattering around his feet">
      <defs>
        <radialGradient id="figure-shade" cx="0.5" cy="0.45" r="0.5">
          <stop offset="0" stop-color="var(--figure-dark)"/>
          <stop offset="0.55" stop-color="var(--figure-dark)" stop-opacity="0.9"/>
          <stop offset="1" stop-color="var(--figure-dark)" stop-opacity="0"/>
        </radialGradient>
      </defs>
      <ellipse class="figure-area" cx="410" cy="570" rx="250" ry="520" fill="url(#figure-shade)"/>
    </svg>

    <h1 class="title" aria-label="The Varnel Cipher">
      <svg viewBox="0 0 800 1200" width="800" height="1200">
        <defs>
          <filter id="worn-ink" x="0" y="0" width="1" height="1">
            <feTurbulence type="fractalNoise" baseFrequency="0.85" numOctaves="2" seed="7" result="noise"/>
            <feColorMatrix in="noise" type="matrix"
              values="0 0 0 0 0  0 0 0 0 0  0 0 0 0 0  0 0 0 14 -8.6" result="specks"/>
            <feComposite in="SourceGraphic" in2="specks" operator="out"/>
          </filter>
        </defs>
        <g filter="url(#worn-ink)" text-anchor="middle">
          <text class="title-line" x="400" y="366">The</text>
          <text class="title-line" x="400" y="530">Varnel</text>
          <text class="title-line" x="400" y="694">Cipher</text>
        </g>
      </svg>
    </h1>

    <p class="author">Jost van Erden</p>
  </main>
</body>
</html>
```